Flyer for Dessert Cafe event launch

Hi
We are launching a new initiative at our cafe - this is the plan:
- We will open Saturday nights to serve desserts, tea and coffee and other after dinner deliciousness (no alcohol)
- Customers stop in and enjoy something sweets on the way home from dinner or movies. We'd decorate the garden with fairy lights, candles and lanterns and create a beautiful and relaxing (and romantic) after dinner atmosphere - maybe a little acoustic guitar
- For the menu we are thinking everything from chocolate mousse and cheesecake to tiramisu and dessert mocktails and even sorbet and gelato.
- The dessert cafe would probably trade from 7pm till 11pm.
Please check out www.brambelkitchen.com for our current branding feel.

We need an A4 flyer designed to promote this new venture.
I want the design to incorporate trees with fairy lights in them - and hearts - as we will be launching on Valentines Day evening (and the heart is part of our branding). Obviously the design needs to be tied in with our current branding - logo attached in various forms I am happy for you to use whichever fits best with your design. I have also attached some images that inspire me for this project - but they don't need to be used.

The following information will need to be included:

On the way home from dinner, or just craving something sweet?
Join us for Dessert!
Unwind - Relax - Indulge
7pm - 11pm every Saturday night
Starting on Valentines Day
All desserts handmade in-house - with love! *** Coffee *** Tea *** Mocktails *** Share platters available ***Gluten Free, Dairy Free and Vegan options *** Take-Away Available
Live Music

2248 Wattleridge Road, Kelvin Flats (five minutes from Marrowby Point)
(03) 5391 8462
www.brambelkitchen.com
Please include the Facebook - Twiiter and Instagram Icons

```html
<!DOCTYPE html>
<html lang="en">
<head>
<meta charset="utf-8">
<title>Brambel Kitchen Café – Join us for Dessert</title>
<link rel="stylesheet" href="https://fonts.googleapis.com/css2?family=Arimo:wght@400;700&family=Marck+Script&family=Mansalva&display=swap">
<style>
  :root {
    --sky-top: #9fb3bd;
    --sky-mid: #b7c2c0;
    --glow-warm: #e6d59a;
    --ground: #cfb98f;
    --brand-red: #d91f2b;
    --ribbon-red: #df2a35;
    --ribbon-dark: #c01a26;
    --ribbon-light: #ea5a62;
    --panel-red: #e02a30;
    --white: #ffffff;
    --outline: #3a3a3a;
  }
  * { margin: 0; padding: 0; box-sizing: border-box; }
  html, body { width: 848px; height: 1200px; overflow: hidden; background: #fff; }
  .flyer {
    position: relative;
    width: 848px;
    height: 1200px;
    overflow: hidden;
    font-family: "Arimo", Arial, sans-serif;
    color: var(--white);
  }
  .scene-photo {
    position: absolute; inset: 0;
    background:
      radial-gradient(circle at 175px 880px, rgba(168,48,43,.55) 0 70px, transparent 120px),
      radial-gradient(ellipse at 380px 800px, rgba(240,220,160,.7), transparent 320px),
      radial-gradient(ellipse at 700px 300px, rgba(255,240,200,.45), transparent 260px),
      linear-gradient(180deg, var(--sky-top) 0%, var(--sky-mid) 40%, var(--glow-warm) 75%, var(--ground) 100%);
  }
  .brand-mark {
    position: absolute; left: -15px; top: -10px;
    width: 260px; height: 260px;
    border: 2px solid var(--white);
    border-radius: 50%;
    display: flex; align-items: center; justify-content: center;
  }
  .brand-name {
    font-size: 26px;
    line-height: 1.1;
    color: var(--brand-red);
    text-align: center;
    white-space: nowrap;
    padding-left: 20px;
  }
  .brand-name small { display: block; font-size: 20px; }
  .headline {
    position: absolute; left: 400px; top: 36px; width: 440px;
    text-align: center;
    font-weight: 400;
    font-size: 38px; line-height: 45px;
    text-shadow: -1px -1px 0 var(--outline), 1px -1px 0 var(--outline), -1px 1px 0 var(--outline), 1px 1px 0 var(--outline), 0 2px 6px rgba(0,0,0,.35);
  }
  .ribbon { position: absolute; left: 0; top: 220px; width: 848px; height: 150px; }
  .ribbon-text {
    position: absolute; left: 0; top: 276px; width: 848px;
    text-align: center;
    font-family: "Marck Script", cursive;
    font-weight: 400;
    font-size: 56px;
    letter-spacing: 1px;
  }
  .launch-date {
    position: absolute; left: 10px; top: 478px; width: 440px;
    text-align: center;
    font-family: "Mansalva", cursive;
    font-size: 52px; line-height: 84px;
    white-space: nowrap;
    color: var(--brand-red);
    text-shadow: 0 0 3px #fff, 0 0 6px #fff, 0 0 10px #fff;
  }
  .offer-panel {
    position: absolute; left: 510px; top: 465px; width: 263px; height: 480px;
    background: var(--panel-red);
    border-left: 2px solid var(--white);
    border-right: 2px solid var(--white);
    text-align: center;
    padding-top: 28px;
  }
  .offer-title {
    font-family: "Marck Script", cursive;
    font-size: 40px; line-height: 46px;
  }
  .offer-sub {
    font-family: "Marck Script", cursive;
    font-size: 22px; margin: 4px 0 34px;
  }
  .offer-list { list-style: none; }
  .offer-list li {
    font-size: 19px; line-height: 23px;
    padding: 8px 0;
    margin: 0 14px;
    border-bottom: 1px solid rgba(255,255,255,.6);
  }
  .offer-list li:last-child { border-bottom: none; }
  .offer-list .sep { font-size: 12px; vertical-align: 2px; }
  .trading-hours {
    position: absolute; left: 28px; top: 1052px;
    font-size: 30px;
  }
  .contact {
    position: absolute; left: 82px; top: 1105px;
    font-size: 17px; line-height: 24px; font-style: normal;
  }
  .social-links { position: absolute; left: 525px; top: 1108px; display: flex; gap: 12px; }
  .social-links span { width: 70px; height: 70px; background: var(--white); border-radius: 6px; display: block; }
</style>
</head>
<body>
<main class="flyer">
  <div class="scene-photo" role="img" aria-label="Soft-focus photo of bare trees strung with fairy lights, with a red gingham fabric heart hanging in the foreground"></div>

  <div class="brand-mark">
    <p class="brand-name">brambel kitchen<small>café</small></p>
  </div>

  <h2 class="headline">On the way<br>home from dinner,<br>or just craving<br>something sweet?</h2>

  <svg class="ribbon" viewBox="0 0 848 150" aria-hidden="true">
    <path d="M0 12 Q424 28 848 14 L848 104 Q424 120 0 138 Z" fill="var(--ribbon-red)"/>
    <path d="M0 12 Q424 28 848 14 L848 30 Q424 44 0 28 Z" fill="var(--ribbon-light)"/>
    <path d="M0 128 Q424 112 848 96 L848 104 Q424 120 0 138 Z" fill="var(--ribbon-dark)"/>
  </svg>
  <h1 class="ribbon-text">Join us for Dessert !</h1>

  <p class="launch-date">Starting on<br>Valentines Day</p>

  <section class="offer-panel">
    <p class="offer-title">All desserts<br>handmade</p>
    <p class="offer-sub">in-house with love!</p>
    <ul class="offer-list">
      <li>Coffee <span class="sep">♥</span> Tea <span class="sep">♥</span> Mocktails</li>
      <li>Share platters available</li>
      <li>Gluten Free <span class="sep">♥</span> Dairy Free<br>and Vegan options</li>
      <li>Take-Away Available</li>
      <li>Unwind <span class="sep">♥</span> Relax <span class="sep">♥</span> Indulge</li>
      <li>Live Music</li>
    </ul>
  </section>

  <p class="trading-hours">7pm - 11pm every Saturday night</p>
  <address class="contact">
    2248 Wattleridge Road, Kelvin Flats<br>
    (five minutes from Marrowby Point)<br>
    (03) 5391 8462 • www.brambelkitchen.com
  </address>

  <div class="social-links" aria-label="Social media">
    <span></span><span></span><span></span>
  </div>
</main>
</body>
</html>
```